Want to learn how to safely prescribe Testosterone, bio-identical hormones and become an expert? I can teach you in 1 weekend!
I have developed and designed Vital Prime Clinic: the worlds first complete Anti-Aging Medical Platform with a "one-stop-learn-workshop tier" where a medical provider can attend my 3-Day Modern Renewal Practice Intensive Course.
During the 3 days the medical provider will become an expert in:
1. Identifying, stratifying and qualifying the appropriate patient for the anti-age hormonal protocol
2. Prescribing Testosterone, Estrogen, Progesterone, Dhea, HcG HgH, both men and women, when appropriate, using my unique and proprietary medically supervised hormone optimization protocol (the protocol as long as my hormone book will be made available to all course attendants)
3. Understanding nutraceuticals and recommending them when appropriate. PeakNovaMIX, the most perfectly developed multi-vitamin, mineral and anti-oxidant pack on the market will be made available for all course attendants to try for free
4. Prescribing a complete and powerful medically optimized weight loss program backed by my proprietary medically supervised protocol and published book (both the protocol and book are available free to all course attendants)
5. Understanding the exercise challenge and understanding what kind of exercise should be prescribed, to whom and in what form. (an extensive proprietary video exercise video library will be available for all course attendants)
6. Upon completion of the workshop each attendee will be proficient enough that upon return to his/her office on Monday, he/she will be able to greatly increase his/her revenue with the knowledge learned.
7. Upon request, the attendee can remain on as affiliate physician of Vital Prime Clinic and learn directly from Dr Varoszny who will help manage each affiliate physician's n.patient until the affiliate physician is confident enough on his/her own

The course will be held on a Saturday and Sunday in Hollywood Florida at the Seabrook Hotel in sunny South Florida

The Course will begin at 930am and end at 3pm each day allowing ample time for sun and fun

I want the email to be STUNNING , to catch the eye of the doctor as this is who I will be sending it to, I want the doctor who opens this email to NOT trash it, to be hypnotized by it, to be intrigued by it, to go ahead and book this course!!!

I will include the logos of Vital Prime Clinic, PeakNovaMix and my weight loss book

Please keep in mind this email MUST be stunning!!! It will be emailed blindly solely to physicians who are notoriously busy and usually trash unknown emails.

I also need to be able to edit the template

Target Market(s)

Doctors

Industry/Entity Type

Medical

Font styles to use
Serif
Sans Serif
Decorative
Script

Colors

Designer to choose colors to be used in the design.

Requirements
Must have
• Stunning colors
• Catchy fonts
• Cool graphics
Nice to have
• an email that is not easily deleted!
• an email that hypnotizes the doctor
• an email that tells the doctor "this is the course I must take!!"
• and email that tells the doctor "if I dont take this course I am a fool"
Should not have
• Negative connotations

```html
<!DOCTYPE html>
<html lang="en">
<head>
<meta charset="utf-8">
<title>Vital Prime Clinic – Weekend Hormone Workshop</title>
<link href="https://fonts.googleapis.com/css2?family=Roboto+Condensed:ital,wght@0,400;0,700;0,900;1,400;1,700&display=swap" rel="stylesheet">
<style>
  :root {
    --black: #000000;
    --red-deep: #b00000;
    --red: #d90000;
    --red-bright: #e30613;
    --white: #ffffff;
    --silver: #d8d8d8;
    --text-soft: #e6e6e6;
    --panel-grey: #3a3a3a;
    --book-brown: #8a5a2b;
  }
  html, body { margin: 0; padding: 0; overflow: hidden; background: var(--black); }
  .canvas {
    position: relative; width: 1200px; height: 1111px; overflow: hidden;
    background: var(--black); font-family: "Roboto Condensed", Arial, sans-serif; color: var(--white);
  }
  .hero-photo {
    position: absolute; left: 0; top: 0; width: 580px; height: 1111px;
    background: radial-gradient(ellipse 55% 70% at 30% 45%, #6a6a6a 0%, #3a3a3a 30%, #161616 60%, #000 85%);
  }
  .column { position: absolute; left: 581px; top: 0; width: 502px; }
  .headline-box {
    background: var(--red-deep); height: 222px; text-align: center;
    padding-top: 26px; box-sizing: border-box; text-transform: uppercase; font-weight: 700;
  }
  .headline-box .question { font-size: 28px; line-height: 25px; letter-spacing: -0.2px; }
  .headline-box .become { font-size: 46px; line-height: 42px; font-weight: 900; color: var(--silver); margin-top: 4px; }
  .headline-box .expert { font-size: 60px; line-height: 52px; font-weight: 900; }
  .promise { text-align: center; margin-top: 36px; text-transform: uppercase; font-weight: 900; }
  .promise .teach { font-size: 58px; line-height: 54px; letter-spacing: -0.5px; }
  .promise .weekend { font-size: 66px; line-height: 58px; color: var(--red-bright); letter-spacing: -1px; }
  .intro-box {
    position: absolute; top: 392px; left: 0; width: 502px; height: 134px;
    background: var(--red); box-sizing: border-box; padding: 22px 50px 0 50px;
    font-weight: 700; text-transform: uppercase; font-size: 16.5px; line-height: 17.6px;
    text-align: justify; text-align-last: center; letter-spacing: -0.2px;
  }
  .outcomes { position: absolute; top: 566px; left: 0; width: 502px; }
  .outcomes h2 { margin: 0 0 20px 33px; font-size: 13px; font-weight: 700; text-transform: uppercase; }
  .outcomes ul { list-style: none; margin: 0; padding: 0 0 0 20px; }
  .outcomes li {
    position: relative; padding-left: 13px; margin-bottom: 11px;
    font-size: 11px; line-height: 11.2px; color: var(--text-soft); letter-spacing: -0.1px;
  }
  .outcomes li::before {
    content: ""; position: absolute; left: 0; top: 0; bottom: 0; width: 4px; background: var(--red-bright);
  }
  .details {
    position: absolute; top: 908px; left: 0; width: 502px; height: 86px;
    background: var(--panel-grey); display: flex; align-items: center; font-size: 10.5px;
  }
  .details .venue { width: 262px; text-align: center; font-style: italic; line-height: 14px; }
  .details .divider { width: 1px; height: 58px; background: var(--white); }
  .details .timing { flex: 1; text-align: center; line-height: 13px; }
  .details .timing strong.label { display: block; font-size: 10.5px; }
  .details .timing em { font-style: italic; }
  .brand-strip {
    position: absolute; top: 994px; left: 0; width: 502px; height: 117px;
    background: var(--white); color: #222;
  }
  .brand-supplement { position: absolute; left: 30px; top: 32px; width: 150px; text-align: center; }
  .brand-supplement .name { font-size: 22px; font-weight: 900; color: var(--red-bright); line-height: 26px; }
  .brand-supplement .tagline { font-size: 6.5px; line-height: 7px; margin-top: 14px; }
  .brand-supplement .tagline b { color: var(--red-bright); }
  .brand-book { position: absolute; left: 218px; top: 14px; width: 60px; text-align: center; }
  .brand-book .cover { width: 55px; height: 80px; margin: 0 auto; background: linear-gradient(160deg, #b07a40, var(--book-brown) 60%, #4a2c10); }
  .brand-book .ribbon { font-size: 5.5px; font-weight: 700; margin-top: 4px; }
  .brand-clinic { position: absolute; left: 318px; top: 44px; display: flex; align-items: center; gap: 6px; }
  .brand-clinic .name { font-size: 18px; font-weight: 400; color: var(--red-bright); }
  .brand-clinic .dot { width: 20px; height: 20px; border: 2px solid var(--red-bright); border-radius: 50%; box-sizing: border-box; }
</style>
</head>
<body>
<div class="canvas">
  <div class="hero-photo" role="img" aria-label="Dramatic low-key photograph of a muscular torso lit from the side against black"></div>

  <div class="column">
    <header class="headline-box">
      <div class="question">Want to learn how to<br>safely prescribe testosterone,<br>bio-identical hormones and</div>
      <div class="become">Become an</div>
      <div class="expert">Expert?</div>
    </header>

    <div class="promise">
      <div class="teach">I can teach you</div>
      <div class="weekend">In 1 weekend!</div>
    </div>

    <div class="intro-box">
      I have developed and designed Vital Prime Clinic: the worlds first complete anti-aging medical platform with a "one-stop-learn-workshop tier" where a medical provider can attend my 3-day Modern Renewal Practice Intensive Course.
    </div>

    <section class="outcomes">
      <h2>During the 3 days the medical provider will become an expert in:</h2>
      <ul>
        <li>Identifying, stratifying and qualifying the appropriate patient for the anti-age hormonal protocol</li>
        <li>Prescribing Testosterone, Estrogen, Progesterone, Dhea, HcG HgH, both men and women, when appropriate, using my unique and proprietary medically supervised hormone optimization protocol (the protocol as long as my hormone book will be made available to all course attendants)</li>
        <li>Understanding nutraceuticals and recommending them when appropriate. PeakNovaMIX, the most perfectly developed multi-vitamin, mineral and anti-oxidant pack on the market will be made available for all course attendants to try for free</li>
        <li>Prescribing a complete and powerful medically optimized weight loss program backed by my proprietary medically supervised protocol and published book (both the protocol and book are available free to all course attendants)</li>
        <li>Understanding the exercise challenge and understanding what kind of exercise should be prescribed, to whom and in what form. (an extensive proprietary video exercise video library will be available for all course attendants)</li>
        <li>Upon completion of the workshop each attendee will be proficient enough that upon return to his/her office on Monday, he/she will be able to greatly increase his/her revenue with the knowledge learned.</li>
        <li>Upon request, the attendee can remain on as affiliate physician of Vital Prime Clinic and learn directly from Dr Varoszny who will help manage each affiliate physician's n.patient until the affiliate physician is confident enough on his/her own.</li>
      </ul>
    </section>

    <div class="details">
      <div class="venue">The course will be held on a <strong>Saturday</strong> and <strong>Sunday</strong><br>in Hollywood Florida at<br>the Seabrook Hotel in sunny South Florida</div>
      <div class="divider"></div>
      <div class="timing">
        <strong class="label">TIMING:</strong>
        begin at <strong>930am</strong> and end at <strong>3pm</strong><br>
        <em>each day allowing ample time for sun and fun</em>
      </div>
    </div>

    <footer class="brand-strip">
      <div class="brand-supplement">
        <div class="name">PeakNovaMix</div>
        <div class="tagline">The <b>PERFECT</b> multi-vitamin, mineral<br>antioxidant and mineral pack</div>
      </div>
      <div class="brand-book">
        <div class="cover" role="img" aria-label="Cover of the weight loss book"></div>
        <div class="ribbon">AVAILABLE NOW!</div>
      </div>
      <div class="brand-clinic">
        <span class="name">Vital Prime Clinic</span>
        <span class="dot"></span>
      </div>
    </footer>
  </div>
</div>
</body>
</html>
```